Coffeeshop menu for filter tip

We want to have a cannabis (coffeeshop) menu in the size 25mm wide x 60mm wide. Some examples attached.

it must have the following text:
Menu

WEED p/g
Velotrine €16
Cinderfox €14
Tide Rambler €14
Marigolden €16
Grand Pelican €14
Copper Comet €14

HASH p/g
Baltic Ember €12
Harbor Velvet€11
Plum Rova €14
Dusk Maple €10

Target Market(s)

tourist in Amsterdam

Requirements
Nice to have
• cannabis sign leaf
• No Cigarettes allowed symbol

```html
<!DOCTYPE html>
<html lang="en">
<head>
<meta charset="utf-8">
<title>Amsterdam Menu</title>
<link rel="stylesheet" href="https://fonts.googleapis.com/css2?family=Arimo:wght@700&family=Cinzel:wght@700;900&display=swap">
<style>
  :root {
    --maroon: #3a0505;
    --panel: rgba(40, 10, 4, 0.72);
    --white: #ffffff;
    --accent: #e4561f;
    --roast-dark: #120804;
    --roast-mid: #4a2410;
    --roast-warm: #7a3e1c;
    --leaf: #4d6a2a;
  }
  * { margin: 0; padding: 0; box-sizing: border-box; }
  html, body { width: 1200px; height: 2885px; overflow: hidden; background: var(--roast-dark); }
  .menu-card { position: relative; width: 1200px; height: 2885px; overflow: hidden; font-family: "Arimo", Arial, sans-serif; color: var(--white); }

  .hero-photo {
    position: absolute; left: 0; top: 0; width: 1200px; height: 780px;
    background:
      radial-gradient(ellipse 360px 240px at 330px 470px, rgba(200,170,140,0.35), transparent 70%),
      radial-gradient(ellipse 420px 320px at 880px 400px, rgba(140,80,35,0.7), transparent 70%),
      radial-gradient(ellipse 700px 260px at 500px 700px, rgba(110,55,25,0.8), transparent 70%),
      linear-gradient(180deg, #0c0604 0%, #2a1409 60%, #4a2410 100%);
  }
  .title-band { position: absolute; left: 0; top: 780px; width: 1200px; height: 203px; background: var(--white); }

  .beans-photo {
    position: absolute; left: 0; top: 983px; width: 1200px; height: 1902px;
    background:
      radial-gradient(ellipse 380px 700px at 1150px 2000px, rgba(77,106,42,0.7), transparent 70%),
      radial-gradient(ellipse 500px 400px at 900px 1750px, rgba(77,106,42,0.45), transparent 70%),
      radial-gradient(ellipse 600px 500px at 300px 400px, rgba(122,62,28,0.6), transparent 70%),
      linear-gradient(180deg, var(--roast-dark) 0%, var(--roast-mid) 40%, #3a1c0c 100%);
  }

  .title-box {
    position: absolute; left: 244px; top: 728px; width: 717px; height: 305px;
    background: var(--maroon); border: 7px solid var(--white); border-radius: 4px;
    text-align: center;
  }
  .title-city { position: absolute; left: 0; right: 0; top: 40px; font-family: "Cinzel", Georgia, serif; font-weight: 700; font-size: 80px; line-height: 1; letter-spacing: 1px; }
  .title-menu { position: absolute; left: 0; right: 0; top: 118px; font-family: "Cinzel", Georgia, serif; font-weight: 900; font-size: 122px; line-height: 1; letter-spacing: 2px; }
  .title-rule { position: absolute; left: 0; top: 0; }

  .frame { position: absolute; border: 7px solid var(--white); }
  .frame-tall { left: 95px; top: 1094px; width: 1010px; height: 1581px; }
  .frame-wide { left: 54px; top: 1140px; width: 1092px; height: 1491px; }
  .price-panel { position: absolute; left: 104px; top: 1103px; width: 992px; height: 1563px; background: var(--panel); }
  .corner-dot { position: absolute; width: 24px; height: 24px; border: 5px solid var(--accent); border-radius: 50%; }

  .section-bar {
    position: absolute; left: 142px; width: 915px; height: 150px; background: var(--white);
    color: var(--maroon); font-size: 88px; font-weight: 700;
    display: flex; justify-content: space-between; align-items: center; padding: 0 32px 0 35px;
  }
  .section-bar.weed { top: 1206px; }
  .section-bar.hash { top: 2003px; }

  .price-list { position: absolute; left: 168px; width: 860px; list-style: none; }
  .price-list.weed { top: 1383px; }
  .price-list.hash { top: 2178px; }
  .price-list li { display: flex; justify-content: space-between; font-size: 84px; line-height: 97.6px; height: 97.6px; }

  .no-smoking { position: absolute; left: 282px; top: 2710px; }
  .no-smoking-label { position: absolute; left: 470px; top: 2735px; font-size: 82px; line-height: 1; }
</style>
</head>
<body>
<main class="menu-card">
  <div class="hero-photo" role="img" aria-label="Steaming cup of coffee on a saucer beside a burlap sack spilling roasted coffee beans"></div>
  <div class="title-band"></div>
  <div class="beans-photo" role="img" aria-label="Close-up of roasted coffee beans with green leaves in the lower right"></div>

  <header class="title-box">
    <h1 class="title-city">AMSTERDAM</h1>
    <div class="title-menu">MENU</div>
    <svg class="title-rule" width="717" height="290" viewBox="0 0 717 290" aria-hidden="true">
      <line x1="204" y1="249" x2="316" y2="249" stroke="#fff" stroke-width="10" stroke-linecap="round"/>
      <circle cx="357" cy="249" r="13" fill="#fff"/>
      <line x1="396" y1="249" x2="506" y2="249" stroke="#fff" stroke-width="10" stroke-linecap="round"/>
    </svg>
  </header>

  <div class="price-panel"></div>
  <div class="frame frame-tall"></div>
  <div class="frame frame-wide"></div>
  <span class="corner-dot" style="left:58px;top:1101px"></span>
  <span class="corner-dot" style="left:1116px;top:1101px"></span>
  <span class="corner-dot" style="left:58px;top:2643px"></span>
  <span class="corner-dot" style="left:1116px;top:2643px"></span>

  <h2 class="section-bar weed"><span>WEED</span><span>p/g</span></h2>
  <ul class="price-list weed">
    <li><span>Velotrine</span><span>€16</span></li>
    <li><span>Cinderfox</span><span>€14</span></li>
    <li><span>Tide Rambler</span><span>€14</span></li>
    <li><span>Marigolden</span><span>€16</span></li>
    <li><span>Grand Pelican</span><span>€14</span></li>
    <li><span>Copper Comet</span><span>€14</span></li>
  </ul>

  <h2 class="section-bar hash"><span>HASH</span><span>p/g</span></h2>
  <ul class="price-list hash">
    <li><span>Baltic Ember</span><span>€12</span></li>
    <li><span>Harbor Velvet</span><span>€11</span></li>
    <li><span>Plum Rova</span><span>€14</span></li>
    <li><span>Dusk Maple</span><span>€10</span></li>
  </ul>

  <svg class="no-smoking" width="144" height="144" viewBox="0 0 144 144" aria-label="No smoking">
    <circle cx="72" cy="72" r="64" fill="none" stroke="#fff" stroke-width="9"/>
    <rect x="22" y="66" width="78" height="18" fill="#fff"/>
    <rect x="104" y="66" width="8" height="18" fill="#fff"/>
    <rect x="116" y="66" width="8" height="18" fill="#fff"/>
    <path d="M98 58 C90 48 108 44 100 32" fill="none" stroke="#fff" stroke-width="6" stroke-linecap="round"/>
    <line x1="27" y1="27" x2="117" y2="117" stroke="#fff" stroke-width="10"/>
  </svg>
  <p class="no-smoking-label">No Sigarets</p>
</main>
</body>
</html>
```